Tarvel Ridge LLC

Need Professional Business cards for New Investment Fund

Target Market(s)

High Quality investors

Industry/Entity Type

Financial

Contact Information for Business Card

Phone Number +1 555 284 6193
Name Pavel Orlinsky
Title Fund Manager
email po@FundTarvel.example
Website www.FundTarvel.example

Colors

Designer to choose colors to be used in the design.

Requirements
Must have
• Must have our Logo and all of the above. Must be made so lettering and loge can be raised

```html
<!DOCTYPE html>
<html lang="en">
<head>
<meta charset="utf-8">
<title>Tarvel Ridge – Business Card</title>
<link rel="stylesheet" href="https://fonts.googleapis.com/css2?family=Lato:wght@400;700;900&display=swap">
<style>
  :root {
    --backdrop: #e4e0da;
    --card: #08090b;
    --card-edge: #121417;
    --pattern-a: #0c0e10;
    --pattern-b: #15181b;
    --green: #62c04a;
    --green-muted: #4a8a3c;
    --grey-text: #8a8d90;
  }
  * { margin: 0; padding: 0; box-sizing: border-box; }
  html, body {
    width: 1200px; height: 800px; overflow: hidden;
    background: var(--backdrop);
    font-family: "Lato", sans-serif;
  }
  .canvas { position: relative; width: 1200px; height: 800px; }
  .card {
    position: absolute; left: 350px; width: 500px; height: 286px;
    border-radius: 18px; background: var(--card); overflow: hidden;
    box-shadow: 0 6px 14px rgba(0,0,0,0.18);
  }
  .card--front { top: 80px; }
  .card--back { top: 434px; }

  .brand {
    position: absolute; left: 66px; top: 126px;
    display: flex; align-items: center; gap: 8px;
  }
  .brand__mark { width: 10px; height: 10px; background: var(--green); }
  .brand__name { color: var(--green); font-weight: 700; font-size: 21px; letter-spacing: 0.2px; }

  .divider {
    position: absolute; left: 222px; top: 86px; width: 1px; height: 112px;
    background: var(--green-muted);
  }
  .person { position: absolute; left: 241px; top: 83px; }
  .person__name { color: var(--green); font-weight: 900; font-size: 23px; line-height: 1; letter-spacing: -0.2px; }
  .person__title { color: var(--grey-text); font-size: 11.5px; margin-top: 7px; }

  .contacts { position: absolute; left: 241px; top: 143px; list-style: none; }
  .contacts__item {
    display: flex; align-items: center; gap: 8px;
    color: var(--grey-text); font-size: 11.5px; height: 20px;
  }
  .contacts__icon { width: 11px; height: 11px; flex: none; }

  .back-pattern {
    position: absolute; inset: 0;
    background: linear-gradient(135deg, var(--pattern-b), var(--pattern-a) 60%, var(--pattern-b));
  }
  .back-brand {
    position: absolute; left: 372px; top: 172px;
    display: flex; align-items: center; gap: 6px;
  }
  .back-brand__mark { width: 7px; height: 7px; background: var(--green); }
  .back-brand__name { color: var(--green); font-weight: 700; font-size: 13px; }
</style>
</head>
<body>
<main class="canvas">
  <section class="card card--front">
    <div class="brand">
      <span class="brand__mark"></span>
      <span class="brand__name">Tarvel Ridge</span>
    </div>
    <div class="divider"></div>
    <div class="person">
      <p class="person__name">Pavel Orlinsky</p>
      <p class="person__title">Fund Manager</p>
    </div>
    <ul class="contacts">
      <li class="contacts__item">
        <svg class="contacts__icon" viewBox="0 0 24 24"><path fill="var(--green)" d="M6.6 10.8a15.1 15.1 0 0 0 6.6 6.6l2.2-2.2c.3-.3.7-.4 1-.2 1.1.4 2.3.6 3.6.6.6 0 1 .4 1 1V20c0 .6-.4 1-1 1A17 17 0 0 1 3 4c0-.6.4-1 1-1h3.5c.6 0 1 .4 1 1 0 1.3.2 2.5.6 3.6.1.3 0 .7-.2 1z"/></svg>
        <span>+1 555 284 6193</span>
      </li>
      <li class="contacts__item">
        <svg class="contacts__icon" viewBox="0 0 24 24"><rect x="2" y="5" width="20" height="14" fill="var(--green)"/><path d="M2 5l10 8 10-8" fill="none" stroke="var(--card)" stroke-width="2"/></svg>
        <span>po@FundTarvel.example</span>
      </li>
      <li class="contacts__item">
        <svg class="contacts__icon" viewBox="0 0 24 24"><g fill="none" stroke="var(--green)" stroke-width="2"><circle cx="12" cy="12" r="10"/><ellipse cx="12" cy="12" rx="4" ry="10"/><path d="M2 12h20M4 7h16M4 17h16"/></g></svg>
        <span>www.FundTarvel.example</span>
      </li>
    </ul>
  </section>

  <section class="card card--back">
    <div class="back-pattern" role="img" aria-label="Faint repeating brand pattern across the card back"></div>
    <div class="back-brand">
      <span class="back-brand__mark"></span>
      <span class="back-brand__name">Tarvel Ridge</span>
    </div>
  </section>
</main>
</body>
</html>
```